Copper and Slate Mists NZ new website!

We are a new online vaping retailer and are looking for an awesome sleek website. We are going to be selling a variety of vaping products and gear. Our logo has just been developed and we would like to keep the website in line with the black, tan a white theme. We would like to trying watermarking or imposing the rottie into the background of the website on the home page, with the page being black and you can see the tan and white colours only.

Coding

Coded - Design and coding required

Number of Pages Required

2 page

Font styles to use
Serif
Sans Serif
Decorative

Requirements
Must have
• A home page and a standard page for products
• Stay in line with the colours in the logo

```html
<!DOCTYPE html>
<html lang="en">
<head>
<meta charset="utf-8">
<title>Copper and Slate Mists NZ</title>
<link href="https://fonts.googleapis.com/css2?family=Montserrat:wght@400;500;600&family=Roboto:wght@400;500&display=swap" rel="stylesheet">
<style>
:root{
  --brown:#a6541a;
  --brown-dark:#7a3c12;
  --orange:#d8842c;
  --tan:#c07a36;
  --ink:#2b2b2b;
  --muted:#666;
  --line:#e3e3e3;
  --white:#fff;
}
*{box-sizing:border-box;margin:0;padding:0}
html,body{width:1200px;height:3634px;overflow:hidden}
body{font-family:"Montserrat",sans-serif;color:var(--ink);background:var(--white);position:relative}
a{color:inherit;text-decoration:none}

.topbar{height:49px;background:var(--brown);display:flex;align-items:center;justify-content:space-between;padding:0 112px;color:#fff;font:500 12px "Roboto",sans-serif}
.social-mini{display:flex;gap:4px}
.social-mini span{width:20px;height:20px;border:1.5px solid #fff;border-radius:50%}
.toplinks{display:flex;gap:22px;align-items:center}
.toplinks .sep{opacity:.7}

.nav{height:117px;position:relative;display:flex;align-items:center;font-size:12.5px;font-weight:500}
.nav a{position:absolute;top:56px}
.nav a.active{color:var(--brown)}
.brand-badge{position:absolute;left:502px;top:0;width:196px;height:196px;border-radius:50%;background:#fff;z-index:3;display:flex;align-items:center;justify-content:center}
.brand-badge span{width:170px;height:170px;border-radius:50%;background:#1d1d1d;color:var(--tan);font:600 17px "Montserrat",sans-serif;text-align:center;display:flex;align-items:center;justify-content:center;line-height:1.3;padding:20px}

.hero{height:649px;position:relative;background:linear-gradient(120deg,#6b4a2c 0%,#2a1e16 40%,#3b3a36 60%,#8a8f95 100%)}
.hero-tag{position:absolute;left:381px;top:405px;width:440px;height:55px;background:var(--tan);opacity:.95;color:#fff;font-size:27px;font-weight:600;display:flex;align-items:center;justify-content:center}
.hero-sub{position:absolute;left:285px;top:470px;width:630px;height:56px;background:rgba(20,20,20,.85);color:#fff;font-size:25px;font-weight:500;display:flex;align-items:center;justify-content:center;letter-spacing:.5px}
.dots{position:absolute;top:611px;left:0;right:0;display:flex;justify-content:center;gap:14px}
.dots i{width:13px;height:13px;border-radius:50%;background:#fff}
.dots i.on{background:var(--brown)}

.section-title{text-align:center;font-size:26px;font-weight:500;letter-spacing:1px}
.section-title::after{content:"";display:block;width:76px;height:3px;background:var(--brown);margin:14px auto 0}

.featured{padding-top:50px;height:1191px}
.grid{position:relative;margin-top:50px;height:1000px}
.card{position:absolute;border:1px solid var(--line);background:#fff}
.card.hot{border:1.5px solid var(--orange)}
.card .name{font-size:15px;font-weight:500}
.card .price{color:var(--brown);font-size:20px;font-weight:500}
.stars{color:var(--orange);font-size:12px;letter-spacing:1px}
.card.wide .stars{position:absolute;left:20px;top:26px}
.card.wide .name{position:absolute;left:20px;top:48px}
.card.wide .name::after{content:"";display:block;width:60px;height:2px;background:var(--orange);margin-top:10px}
.card.wide .price{position:absolute;left:20px;top:92px}
.card.tall{text-align:center}
.card.tall .shot{margin:24px auto 0;width:180px;height:150px}
.card.tall .price{margin-top:16px}
.card.tall .name{margin-top:12px}
.card.tall .stars{margin-top:8px}
.shot{background:radial-gradient(ellipse at center,#8a8a8a 0%,#cfcfcf 55%,#f4f4f4 80%);border-radius:6px}
.sale{position:absolute;right:26px;top:20px;width:68px;height:68px;border-radius:50%;background:var(--brown);color:#fff;font-size:13px;font-weight:500;display:flex;align-items:center;justify-content:center}
.tools{position:absolute;left:14px;top:190px;display:flex;flex-direction:column;gap:9px}
.tools span{width:30px;height:30px;border:1px solid #ccc;border-radius:5px;display:flex;align-items:center;justify-content:center}

.promo{height:436px;background:linear-gradient(135deg,#5a3516 0%,#a25c22 45%,#c47a30 70%,#6b3c16 100%);color:#fff;text-align:center;padding-top:108px}
.promo h2{font-size:40px;font-weight:600;letter-spacing:.5px}
.promo p{font-size:26px;font-weight:400;margin-top:16px;letter-spacing:.5px}
.promo .btn{display:inline-block;margin-top:30px;border:1.5px solid #fff;border-radius:32px;padding:22px 27px;font-size:15px;font-weight:500}

.blog{height:546px;padding-top:52px}
.posts{position:relative;margin-top:48px}
.post{position:absolute;top:0;width:468px;height:362px;border:1px solid var(--line)}
.post .photo{height:220px;position:relative;background:linear-gradient(135deg,#2d3033,#6f7378 60%,#1e2022)}
.post .date{position:absolute;left:0;bottom:0;background:var(--brown);color:#fff;font-size:14px;padding:9px 26px 9px 16px;clip-path:polygon(0 0,88% 0,100% 100%,0 100%)}
.post h3{font-size:15px;font-weight:500;margin:34px 22px 0}
.post p{font:400 12px/26px "Roboto",sans-serif;color:var(--muted);margin:8px 22px 0}
.post p a{color:var(--brown)}

.newsletter{height:304px;background:var(--orange);color:#fff;text-align:center;padding-top:40px}
.newsletter h2{font-size:24px;font-weight:500;letter-spacing:1px}
.newsletter p{font:400 11px/22px "Roboto",sans-serif;width:690px;margin:14px auto 0}
.subscribe{display:flex;width:638px;margin:38px auto 0;height:46px}
.subscribe input{flex:1;border:0;padding:0 20px;font:400 12px "Roboto",sans-serif;border-radius:3px 0 0 3px}
.subscribe button{width:162px;border:0;background:var(--brown);color:#fff;font:500 14px "Montserrat",sans-serif;border-radius:0 3px 3px 0}

.footer{height:275px;position:relative;border-bottom:1px solid var(--line)}
.fcol{position:absolute;top:50px}
.fcol h4{font-size:14px;font-weight:500;margin-bottom:22px}
.fcol ul{list-style:none;font:400 11.5px "Roboto",sans-serif;color:var(--muted)}
.fcol li{height:25.5px;padding-left:27px;position:relative}
.fcol li::before{content:"";position:absolute;left:2px;top:4px;border-left:5px solid #666;border-top:4px solid transparent;border-bottom:4px solid transparent}
.cards{display:flex;gap:3px}
.cards span{width:41px;height:26px;border-radius:3px;border:1px solid #bbb;background:#e9e9e9}
.cards span:nth-child(2){background:#d9d9d9}
.fsocial{display:flex;gap:6px;margin-top:48px}
.fsocial span{width:31px;height:31px;border:1.5px solid #777;border-radius:50%}
.contact li{padding-left:29px;line-height:14px;height:auto;margin-bottom:14px}
.contact li::before{display:none}
.contact svg{position:absolute;left:0;top:0}
.contact a{color:var(--brown);text-decoration:underline}
.copyright{text-align:center;font:400 12px "Roboto",sans-serif;color:var(--muted);padding-top:18px}
</style>
</head>
<body>

<header class="topbar">
  <div class="social-mini"><span></span><span></span><span></span><span></span><span></span></div>
  <nav class="toplinks">
    <a href="#">LOGIN</a><span class="sep">|</span>
    <a href="#">REGISTER</a><span class="sep">|</span>
    <a href="#">COMPARE</a><span class="sep">|</span>
    <a href="#">CART</a><span class="sep">|</span>
    <a href="#">SEARCH</a>
  </nav>
</header>

<nav class="nav">
  <a href="#" class="active" style="left:156px">HOME</a>
  <a href="#" style="left:251px">ABOUT US</a>
  <a href="#" style="left:372px">SERVICES</a>
  <div class="brand-badge"><span>Copper &amp; Slate Mists NZ</span></div>
  <a href="#" style="left:722px">PRODUCTS</a>
  <a href="#" style="left:849px">GALLERY</a>
  <a href="#" style="left:961px">CONTACT US</a>
</nav>

<section class="hero" role="img" aria-label="Photo of two dogs resting on a wooden porch">
  <div class="hero-tag">COPPER &amp; SLATE MISTS NZ</div>
  <div class="hero-sub">SED UT PERSPICIATIS UNDE OMNIS ISTE</div>
  <div class="dots"><i></i><i class="on"></i><i></i></div>
</section>

<section class="featured">
  <h2 class="section-title">FEATURED PRODUCTS</h2>
  <div class="grid">
    <!-- row 1 -->
    <article class="card wide hot" style="left:110px;top:0;width:473px;height:321px">
      <div class="name" style="top:26px">PRODUCT NAME</div>
      <div class="price" style="top:70px">$ 29.99</div>
      <div class="sale">SALE</div>
      <div class="shot" style="position:absolute;left:110px;top:120px;width:320px;height:120px" role="img" aria-label="Vaporizer pen with dried herb"></div>
      <div class="tools"><span></span><span></span><span></span></div>
    </article>
    <article class="card tall" style="left:596px;top:0;width:241px;height:321px">
      <div class="shot" role="img" aria-label="Vape cartridge on herb"></div>
      <div class="price">$ 29.99</div><div class="name">PRODUCT NAME</div><div class="stars">★★★★★</div>
    </article>
    <article class="card tall" style="left:847px;top:0;width:241px;height:321px">
      <div class="shot" role="img" aria-label="Three vape mods in colours"></div>
      <div class="price">$ 29.99</div><div class="name">PRODUCT NAME</div><div class="stars">★★★★★</div>
    </article>
    <!-- row 2 -->
    <article class="card wide" style="left:110px;top:335px;width:363px;height:321px">
      <div class="stars">★★★★★</div><div class="name">PRODUCT NAME</div><div class="price">$ 29.99</div>
      <div class="shot" style="position:absolute;left:70px;top:125px;width:270px;height:140px" role="img" aria-label="Box mod with tank"></div>
    </article>
    <article class="card wide" style="left:484px;top:335px;width:604px;height:321px">
      <div class="stars">★★★★★</div><div class="name">PRODUCT NAME</div><div class="price">$ 29.99</div>
      <div class="shot" style="position:absolute;left:140px;top:70px;width:400px;height:200px" role="img" aria-label="Two vape pens"></div>
    </article>
    <!-- row 3 -->
    <article class="card wide" style="left:110px;top:671px;width:473px;height:321px">
      <div class="stars">★★★★★</div><div class="name">PRODUCT NAME</div><div class="price">$ 29.99</div>
      <div class="shot" style="position:absolute;left:150px;top:40px;width:270px;height:240px" role="img" aria-label="Vape devices and e-liquid bottles"></div>
    </article>
    <article class="card tall" style="left:596px;top:671px;width:241px;height:321px">
      <div class="shot" role="img" aria-label="E-liquid bottles and vape pen"></div>
      <div class="price">$ 29.99</div><div class="name">PRODUCT NAME</div><div class="stars">★★★★★</div>
    </article>
    <article class="card tall" style="left:847px;top:671px;width:241px;height:321px">
      <div class="shot" role="img" aria-label="Compact box mod"></div>
      <div class="price">$ 29.99</div><div class="name">PRODUCT NAME</div><div class="stars">★★★★★</div>
    </article>
  </div>
</section>

<section class="promo" role="img" aria-label="Warm-toned close-up of vape devices on a wooden surface">
  <h2>COPPER &amp; SLATE MISTS NZ</h2>
  <p>SED UT PERSPICIATIS UNDE OMNIS ISTE NATUS ERROR</p>
  <a href="#" class="btn">CLICK HERE FOR MORE INFO</a>
</section>

<section class="blog">
  <h2 class="section-title">LATEST BLOG</h2>
  <div class="posts">
    <article class="post" style="left:113px">
      <div class="photo" role="img" aria-label="Vape pens with herb on dark background"><span class="date">02 March 2019</span></div>
      <h3>SED UT PERSPICIATIS UNDE OMNIS</h3>
      <p>Nemo enim ipsam voluptatem quia voluptas sit aspernatur aut odit aut fugit, eos qui ratione voluptatem sequi nesciunt. <a href="#">READ MORE</a></p>
    </article>
    <article class="post" style="left:619px">
      <div class="photo" role="img" aria-label="Assorted vape mods laid out on blue fabric" style="background:linear-gradient(135deg,#1f2a3a,#3d4d63 55%,#161c26)"><span class="date">02 March 2019</span></div>
      <h3>SED UT PERSPICIATIS UNDE OMNIS</h3>
      <p>Nemo enim ipsam voluptatem quia voluptas sit aspernatur aut odit aut fugit, eos qui ratione voluptatem sequi nesciunt. <a href="#">READ MORE</a></p>
    </article>
  </div>
</section>

<section class="newsletter">
  <h2>SUBSCRIBE TO OUR NEWSLETTER</h2>
  <p>Sed ut perspiciatis unde omnis iste natus error sit voluptatem accusantium doloremque laudantium, totam rem aperiam, eaque ipsa quae ab illo inventore veritatis et quasi architecto beatae vitae dicta sunt explicabo.</p>
  <form class="subscribe"><input type="text" placeholder="Enter Your Email Id :"><button type="button">SUBSCRIBE</button></form>
</section>

<footer class="footer">
  <div class="fcol" style="left:113px">
    <h4>PAYMENTS ACCEPTED</h4>
    <div class="cards"><span></span><span></span><span></span><span></span></div>
    <div class="fsocial"><span></span><span></span><span></span><span></span><span></span></div>
  </div>
  <div class="fcol" style="left:337px">
    <h4>INFORMATION</h4>
    <ul><li>Sitemap</li><li>Shipping &amp; Returns</li><li>Privacy Notice</li><li>Conditions of Use</li><li>About us</li><li>Contact us</li></ul>
  </div>
  <div class="fcol" style="left:523px">
    <h4>CUSTOMER SERVICE</h4>
    <ul><li>Search</li><li>Blog</li><li>Recently viewed products</li><li>Compare products list</li><li>New products</li></ul>
  </div>
  <div class="fcol" style="left:746px">
    <h4>MY ACCOUNT</h4>
    <ul><li>My account</li><li>Orders</li><li>Addresses</li><li>Shopping cart</li><li>Wishlist</li></ul>
  </div>
  <div class="fcol contact" style="left:895px;top:54px">
    <h4>CONTACT US</h4>
    <ul>
      <li><svg width="13" height="12" viewBox="0 0 13 12"><rect x="1" y="4" width="11" height="7" rx="1" fill="#777"/><path d="M1 4 Q6.5 -1 12 4" stroke="#777" stroke-width="2" fill="none"/></svg>(000)-121-1231 (Phone)</li>
      <li><svg width="13" height="12" viewBox="0 0 13 12"><rect x="3" y="0" width="7" height="4" fill="#777"/><rect x="0" y="4" width="13" height="6" rx="1" fill="#777"/></svg>(000)-121-1231 &nbsp;(Fax)</li>
      <li><svg width="13" height="10" viewBox="0 0 13 10"><rect x="0" y="0" width="13" height="10" fill="#777"/><path d="M0 0 L6.5 6 L13 0" stroke="#fff" fill="none"/></svg><a href="#">info@copperslatemists.co.nz</a></li>
      <li><svg width="10" height="14" viewBox="0 0 10 14"><path d="M5 0 C2 0 0 2 0 5 C0 9 5 14 5 14 C5 14 10 9 10 5 C10 2 8 0 5 0Z" fill="#777"/><circle cx="5" cy="5" r="2" fill="#fff"/></svg>#1452 Lorem Ipsum Dummy<br>Text Lorem Ipsum</li>
    </ul>
  </div>
</footer>
<p class="copyright">© Copyright 2019 Copper and Slate Mists NZ.All Rights Reserved</p>

</body>
</html>
```